Modern Quillby Tree Care Website

I need a website for a full service Tree Care company. The company provides tree pruning, tree removal, tree preservation, emergency services, stump grinding, and emergency tree services.

Target Market(s)

Customers that need tree services

Industry/Entity Type

Landscaping, Tree Services

Coding

Coded - Design and coding required

Number of Pages Required

5+ page

Font styles to use
Sans Serif

Requirements
Must have
• Good clean design that showcases the services the company provides.
Nice to have
• Services page; contact form, blog, home page, about page

```html
<!DOCTYPE html>
<html lang="en">
<head>
<meta charset="utf-8">
<title>Quillby Tree Care</title>
<link rel="stylesheet" href="https://fonts.googleapis.com/css2?family=Orbitron:wght@900&family=Roboto:wght@400;500;700&display=swap">
<style>
:root{
  --green:#8cc63f;
  --green-dark:#6fa52a;
  --orange:#f9ae3c;
  --brown:#c49a6c;
  --ink:#111111;
  --text:#333333;
  --white:#ffffff;
  --soil:#2a211b;
}
*{margin:0;padding:0;box-sizing:border-box}
html,body{width:1200px;height:4342px;overflow:hidden}
body{position:relative;font-family:"Roboto",sans-serif;color:var(--text);background:var(--white)}
.abs{position:absolute}
.display{font-family:"Orbitron",sans-serif;font-weight:900;color:var(--ink);letter-spacing:2px}
.eyebrow{font-size:15px;color:var(--green);font-weight:500}
.btn{position:absolute;display:flex;align-items:center;justify-content:center;background:var(--green);color:var(--ink);border-radius:20px;font-size:14px;font-weight:500}
.media{position:absolute}

/* hero */
.hero{position:absolute;left:0;top:0;width:1200px;height:720px;overflow:hidden;
  background:linear-gradient(180deg,#7fb3e6 0%,#a9cdef 45%,#d3e3f1 80%,#c9c1ad 100%)}
.hero .media{left:0;top:0;width:1200px;height:720px;background:linear-gradient(110deg,rgba(90,70,50,.55) 0%,rgba(150,120,90,.25) 30%,rgba(255,255,255,0) 55%,rgba(110,95,70,.3) 100%)}
.nav{position:absolute;left:110px;top:17px;width:977px;height:87px;background:#f4f6f8;display:flex;align-items:center}
.nav .brand{position:absolute;left:0;top:0;width:297px;height:87px;background:var(--green);clip-path:polygon(0 0,100% 0,86% 100%,0 100%);display:flex;align-items:center;padding-left:22px;gap:12px}
.brand .mark{width:36px;height:36px;background:var(--ink)}
.brand .name{font-size:28px;font-weight:700;color:var(--ink);line-height:1}
.brand .name small{display:block;font-size:16px;font-weight:400;letter-spacing:4px;margin-top:4px}
.nav ul{position:absolute;left:323px;top:34px;list-style:none;display:flex;gap:26px;font-size:15px;color:var(--ink)}
.nav .login{left:838px;top:27px;width:117px;height:37px}
.hero-copy{position:absolute;right:113px;top:258px;text-align:right}
.hero-copy .welcome{font-size:28px;color:var(--ink)}
.hero-copy .big{font-size:66px;font-weight:700;color:var(--ink);line-height:1;margin-top:8px;letter-spacing:1px}
.hero-copy .sub{font-size:34px;color:var(--ink);letter-spacing:1px}
.hero-copy p{font-size:15px;line-height:25px;color:var(--ink);margin-top:10px}
.hero .start{left:972px;top:472px;width:115px;height:36px;font-size:13px}

/* about */
.about-frame{left:140px;top:752px;width:380px;height:368px;border:2px solid var(--green)}
.about-img{left:128px;top:740px;width:381px;height:367px;background:linear-gradient(135deg,#6b5a44,#a08a6c 45%,#d8c9ae 80%,#e8e2d6)}
.about-text{left:600px;top:722px;width:488px}
.about-text h2{font-size:30px;margin-top:8px}
.about-text p{font-size:14px;line-height:25.5px;text-align:justify;margin-top:26px;color:var(--ink)}
.about-text p+p{margin-top:16px}
.about .more{left:600px;top:1051px;width:116px;height:37px}

/* services */
.svc-bg{left:0;top:1213px;width:1200px;height:580px}
.svc-head{left:0;top:1238px;width:1200px;text-align:center}
.svc-head h2{font-size:31px;margin-top:6px}
.card{position:absolute;top:1362px;width:289px;height:390px;background:var(--white);box-shadow:0 3px 8px rgba(0,0,0,.25);text-align:center}
.card .media{left:0;top:0;width:289px;height:196px}
.card .badge{position:absolute;left:99px;top:152px;width:92px;height:72px}
.card h3{position:absolute;top:250px;width:100%;font-size:21px;font-weight:500;color:var(--ink)}
.card p{position:absolute;top:283px;left:20px;right:20px;font-size:14px;line-height:25px}
.card a{position:absolute;top:337px;left:0;right:0;font-size:15px;font-weight:500;color:var(--ink);text-decoration:underline}
.arrow{position:absolute;top:1508px;width:24px;height:40px}

/* why */
.why-head{left:0;top:1855px;width:1200px;text-align:center}
.why-head h2{font-size:31px;margin-top:6px}
.why-art{left:388px;top:1980px;width:488px;height:540px;border-radius:50%;
  background:radial-gradient(circle at 50% 45%,#8cc63f 0%,#b9d98a 30%,#f9ae3c 55%,rgba(255,255,255,0) 72%)}
.benefit{position:absolute;width:300px}
.benefit h4{font-size:16px;font-weight:700;color:var(--ink)}
.benefit p{font-size:14px;line-height:25px;margin-top:4px}
.benefit.left{text-align:right}

/* blog */
.blog{left:0;top:2607px;width:1200px;height:689px;background:var(--green)}
.blog-head{left:0;top:2662px;width:1200px;text-align:center}
.blog-head span{font-size:15px;color:var(--ink)}
.blog-head h2{font-size:31px;margin-top:6px}
.post{position:absolute;top:2785px;width:301px}
.post .media{position:relative;width:301px;height:309px;background:linear-gradient(160deg,#3f4a2f,#8a7a5c 50%,#c86f2a 70%,#5b4a36)}
.post h3{font-size:25px;font-weight:400;line-height:33px;color:var(--ink);margin-top:18px}
.post a{display:block;font-size:15px;font-weight:500;color:var(--ink);text-decoration:underline;margin:4px 0 0 4px}

/* contact */
.contact{left:0;top:3296px;width:1200px;height:1046px;
  background:linear-gradient(180deg,#6f9fd6 0%,#a9c8e8 30%,#dfe9ef 55%,#9cc84a 68%,#4f8a1f 74%,#2a211b 76%,#1e1814 100%)}
.contact-tree{left:740px;top:3360px;width:390px;height:440px;border-radius:48% 52% 20% 20%;background:radial-gradient(circle at 50% 35%,#6ea33a,#3f6e1e 60%,rgba(63,110,30,0) 72%)}
.contact-head{left:110px;top:3384px}
.contact-head span{font-size:15px;color:var(--ink)}
.contact-head h2{font-size:31px;margin-top:8px}
.field{position:absolute;border:1px solid #3a3a3a;background:rgba(255,255,255,.55);font-size:15px;color:#333;padding:14px 12px}
.submit{left:110px;top:3746px;width:114px;height:35px;font-size:13px}

/* footer */
.foot-brand{left:111px;top:3993px;display:flex;align-items:center;gap:12px}
.foot-brand .mark{width:52px;height:52px;background:var(--white)}
.foot-brand .name{font-size:40px;font-weight:700;color:var(--white);line-height:1}
.foot-brand .name small{display:block;font-size:20px;font-weight:400;letter-spacing:5px;margin-top:4px}
.foot-col h4{font-family:"Orbitron",sans-serif;font-weight:900;font-size:19px;color:var(--white);letter-spacing:1px}
.quick{left:422px;top:3992px}
.quick ul{list-style:none;margin-top:22px}
.quick li{font-size:15px;font-weight:500;color:var(--white);height:42px}
.reach{left:635px;top:3992px}
.reach .item{position:absolute;left:0;width:260px;display:flex;gap:12px;align-items:center;color:var(--white)}
.reach .item b{display:block;font-size:19px;font-weight:500}
.reach .item span{font-size:15px;font-weight:500}
.reach .ico{width:44px;height:44px;border-radius:50%;background:var(--green);display:flex;align-items:center;justify-content:center;flex:none}
.follow{left:937px;top:3992px}
.social{position:absolute;top:4035px;width:42px;height:42px;border-radius:50%;background:var(--white)}
.copy{left:0;top:4282px;width:1200px;text-align:center;font-size:14px;color:var(--white)}
</style>
</head>
<body>

<section class="hero">
  <div class="media" role="img" aria-label="Arborist in safety gear cutting a branch high in a tree against blue sky"></div>
  <svg class="abs" style="left:0;top:560px" width="1200" height="160" viewBox="0 0 1200 160">
    <path d="M0 80 C300 30 800 40 1200 140 L1200 160 L0 160 Z" fill="#ffffff"/>
  </svg>
  <nav class="nav">
    <div class="brand"><span class="mark"></span><span class="name">QUILLBY<small>TREE CARE</small></span></div>
    <ul><li>HOME</li><li>ABOUT US</li><li>SERVICES</li><li>BLOG</li><li>CONTACT US</li></ul>
    <span class="btn login">LOGIN</span>
  </nav>
  <div class="hero-copy">
    <div class="welcome">WELCOME TO</div>
    <div class="big">QUILLBY</div>
    <div class="sub">TREE CARE</div>
    <p>Lorem ipsum dolor sit amet, consectetur adipiscing elit, sed do<br>eiusmod tempor incididunt ut labore et dolore magna aliqua.</p>
  </div>
  <span class="btn start">GET STARTED</span>
</section>

<section class="about">
  <div class="abs about-frame"></div>
  <div class="media about-img" role="img" aria-label="Worker with chainsaw felling a large tree trunk"></div>
  <div class="abs about-text">
    <div class="eyebrow">WHO WE ARE</div>
    <h2 class="display">ABOUT US</h2>
    <p>At Quillby Tree Care, we are more than just a tree service company, we are stewards of our beautiful trees. With a passion deeply rooted in arboriculture, we embark on a mission to promote the health, beauty, and safety of your trees and landscapes.</p>
    <p>Whether it's expert tree trimming to enhance aesthetics, meticulous tree removal to mitigate hazards, or comprehensive tree health assessments to ensure safety, we approach each task with unwavering dedication and attention to detail.</p>
  </div>
  <span class="btn more">READ MORE</span>
</section>

<section class="services">
  <svg class="abs svc-bg" width="1200" height="580" viewBox="0 0 1200 580">
    <polygon points="0,0 477,0 0,578" fill="#c49a6c"/>
    <polygon points="728,5 1200,5 1200,578" fill="#f9ae3c"/>
  </svg>
  <div class="abs svc-head"><div class="eyebrow">WHAT WE DO</div><h2 class="display">OUR SERVICES</h2></div>
  <svg class="arrow" style="left:60px" viewBox="0 0 24 40"><path d="M18 6 L6 20 L18 34" fill="none" stroke="#555" stroke-width="4"/></svg>
  <svg class="arrow" style="left:1104px" viewBox="0 0 24 40"><path d="M6 6 L18 20 L6 34" fill="none" stroke="#111" stroke-width="4"/></svg>

  <article class="card" style="left:111px">
    <div class="media" role="img" aria-label="Worker pruning a hedge with a pole saw" style="background:linear-gradient(180deg,#4d7a2c,#8aa65a 60%,#5c7a3a)"></div>
    <svg class="badge" viewBox="0 0 92 72"><polygon points="46,0 92,72 0,72" fill="#fff"/><circle cx="46" cy="44" r="14" fill="#8cc63f"/></svg>
    <h3>TREE PRUNING</h3>
    <p>ametnsectetur adipiscing elit, sed do eiusmod tempor.</p>
    <a>READ MORE</a>
  </article>
  <article class="card" style="left:453px">
    <div class="media" role="img" aria-label="Crew removing a felled tree trunk beside a house" style="background:linear-gradient(180deg,#a8b3bd,#7a6a55 55%,#4d6b2e)"></div>
    <svg class="badge" viewBox="0 0 92 72"><polygon points="46,0 92,72 0,72" fill="#fff"/><circle cx="46" cy="44" r="14" fill="#8cc63f"/></svg>
    <h3>TREE REMOVAL</h3>
    <p>ametnsectetur adipiscing elit, sed do eiusmod tempor.</p>
    <a>READ MORE</a>
  </article>
  <article class="card" style="left:795px">
    <div class="media" role="img" aria-label="Gardeners planting young trees in soil" style="background:linear-gradient(180deg,#3e5a2a,#6b7d4a 50%,#4a3a2a)"></div>
    <svg class="badge" viewBox="0 0 92 72"><polygon points="46,0 92,72 0,72" fill="#fff"/><circle cx="46" cy="44" r="14" fill="#f9ae3c"/></svg>
    <h3>TREE PRESERVATION</h3>
    <p>ametnsectetur adipiscing elit, sed do eiusmod tempor.</p>
    <a>READ MORE</a>
  </article>
</section>

<section class="why">
  <div class="abs why-head"><div class="eyebrow">OUR BENEFITS</div><h2 class="display">WHY CHOOSE US</h2></div>
  <div class="media why-art" role="img" aria-label="Illustrated tree of green and orange circles holding benefit icons"></div>

  <div class="benefit left" style="left:110px;top:2038px"><h4>LOCALLY OWNED &amp; OPERATED</h4><p>Lorem ipsum dolor sit amet, onsad<br>sed do eiusmod tempor aliqua.</p></div>
  <div class="benefit left" style="left:60px;top:2170px"><h4>24-HOURS EMERGENCY<br>SERVICES</h4><p>Lorem ipsum dolor sit amet, onsad<br>sed do eiusmod tempor aliqua.</p></div>
  <div class="benefit left" style="left:95px;top:2318px"><h4>LICENSED AND INSURED</h4><p>Lorem ipsum dolor sit amet, consectetur<br>adipiscing elit, sed do eiusmod tempor<br>aliqua.</p></div>

  <div class="benefit" style="left:832px;top:2035px"><h4>PROFESSIONAL WORK</h4><p>Lorem ipsum dolor sit amet, onsad<br>sed do eiusmod tempor aliqua.</p></div>
  <div class="benefit" style="left:881px;top:2168px"><h4>SAFETY IS OUR NO.1<br>PRIORITY</h4><p>Lorem ipsum dolor sit amet,<br>sed do eiusmod tempor aliqua.</p></div>
  <div class="benefit" style="left:848px;top:2318px"><h4>FREE ESTIMATES</h4><p>Lorem ipsum dolor sit amet,<br>sed do eiusmod tempor aliqua.</p></div>
  <div class="benefit" style="left:746px;top:2436px"><h4>LICENSED ARBORIST ON STAFF</h4><p>Lorem ipsum dolor sit amet,<br>sed do eiusmod tempor aliqua.</p></div>
</section>

<section class="abs blog"></section>
<div class="abs blog-head"><span>OUR BLOG</span><h2 class="display">OUR LATEST NEWS</h2></div>
<article class="post" style="left:110px">
  <div class="media" role="img" aria-label="Gloved hands running a chainsaw through a log"></div>
  <h3>Lorem ipsum dolor sit amet,sed do aliqua.</h3><a>VIEW DETAILS</a>
</article>
<article class="post" style="left:448px">
  <div class="media" role="img" aria-label="Arborist in orange safety gear cutting at a tree base"></div>
  <h3>Lorem ipsum dolor sit amet,sed do aliqua.</h3><a>VIEW DETAILS</a>
</article>
<article class="post" style="left:786px">
  <div class="media" role="img" aria-label="Chainsaw cutting into a tree trunk"></div>
  <h3>Lorem ipsum dolor sit amet,sed do aliqua.</h3><a>VIEW DETAILS</a>
</article>

<section class="abs contact" role="img" aria-label="Lone tree on a green hill under blue sky above dark soil"></section>
<div class="media contact-tree" role="img" aria-label="Large leafy tree on the hilltop"></div>
<div class="abs contact-head"><span>CONTACT US</span><h2 class="display">GET IN TOUCH</h2></div>
<div class="field" style="left:111px;top:3491px;width:302px;height:48px">First Name</div>
<div class="field" style="left:430px;top:3491px;width:301px;height:48px">Last Name</div>
<div class="field" style="left:111px;top:3562px;width:302px;height:48px">Email</div>
<div class="field" style="left:430px;top:3562px;width:301px;height:48px">Phone No</div>
<div class="field" style="left:111px;top:3633px;width:620px;height:88px">Message</div>
<span class="btn submit">SUBMIT</span>

<footer>
  <div class="abs foot-brand"><span class="mark"></span><span class="name">QUILLBY<small>TREE CARE</small></span></div>
  <div class="abs foot-col quick"><h4>Quick Links</h4>
    <ul><li>Home</li><li>About Us</li><li>Services</li><li>Blog</li><li>Contact Us</li></ul>
  </div>
  <div class="abs foot-col reach"><h4>Contact Us</h4>
    <div class="item" style="top:45px"><span class="ico"><svg width="20" height="16" viewBox="0 0 20 16"><rect x="1" y="1" width="18" height="14" rx="2" fill="#fff"/><path d="M1 2 L10 9 L19 2" fill="none" stroke="#6fa52a" stroke-width="2"/></svg></span><div><b>Email:</b><span>info@quillbytreecare.com</span></div></div>
    <div class="item" style="top:123px"><span class="ico"><svg width="20" height="20" viewBox="0 0 24 24"><path d="M6.6 10.8a15 15 0 0 0 6.6 6.6l2.2-2.2a1 1 0 0 1 1-.25 11.4 11.4 0 0 0 3.6.6 1 1 0 0 1 1 1V20a1 1 0 0 1-1 1A17 17 0 0 1 3 4a1 1 0 0 1 1-1h3.5a1 1 0 0 1 1 1c0 1.25.2 2.45.6 3.6a1 1 0 0 1-.25 1z" fill="#fff"/></svg></span><div><b>Phone No:</b><span>(555) 014-2739</span></div></div>
    <div class="item" style="top:202px"><span class="ico"><svg width="18" height="24" viewBox="0 0 18 24"><path d="M9 0a9 9 0 0 0-9 9c0 7 9 15 9 15s9-8 9-15a9 9 0 0 0-9-9z" fill="#fff"/><circle cx="9" cy="9" r="3.5" fill="#8cc63f"/></svg></span><div><b>Location:</b><span>Quillby Tree Care, USA</span></div></div>
  </div>
  <div class="abs foot-col follow"><h4>Follow Us</h4></div>
  <span class="social" style="left:938px"></span>
  <span class="social" style="left:992px"></span>
  <span class="social" style="left:1046px"></span>
  <div class="abs copy">Copyright © 2024 Quillby Tree Care | All Rights Reserved</div>
</footer>

</body>
</html>
```